BRC Business cards

We are a medium sized property company based in London and require a logo, Business card which reflects a professional company and incorporates our catchy name.

Our statement is (Building for the future) we like colours such as royal blue, greens and light browns but will look at anything.

Contact Information for Business Card

Brookcrest Estates Limited
Unit 4, 15-17 Farrowby Lane
London
SE22 7QN

Web: www.brookcrestestates-example.com

Email: brookcrestltd@mailbox-example.com

Telephone: +44-208-555-0142
Fax: +44-208-555-0187

```html
<!DOCTYPE html>
<html lang="en">
<head>
<meta charset="utf-8">
<title>Brookcrest Estates Limited – Business Card</title>
<link rel="stylesheet" href="https://fonts.googleapis.com/css2?family=Bree+Serif&display=swap">
<style>
  :root {
    --royal: #0b4ea8;
    --royal-light: #1664c0;
    --royal-mid: #0f58b3;
    --navy: #06204f;
    --navy-deep: #020c24;
    --black: #000000;
    --cyan: #1ba6e6;
    --white: #ffffff;
  }
  html, body {
    margin: 0;
    padding: 0;
    width: 1200px;
    height: 791px;
    overflow: hidden;
    background: var(--white);
  }
  .card {
    position: relative;
    width: 1200px;
    height: 791px;
    overflow: hidden;
    background: var(--royal);
    font-family: "Bree Serif", Georgia, serif;
  }
  .card-backdrop {
    position: absolute;
    inset: 0;
  }
  .brand {
    position: absolute;
    left: 58px;
    top: 150px;
    display: flex;
    align-items: center;
    gap: 18px;
  }
  .brand-square {
    width: 44px;
    height: 44px;
    background: var(--white);
  }
  .brand-name {
    margin: 0;
    color: var(--white);
    font-size: 62px;
    font-weight: 400;
    letter-spacing: 1px;
    line-height: 1;
  }
  .contact {
    position: absolute;
    left: 450px;
    top: 420px;
    color: var(--white);
  }
  .company-name {
    margin: 0 0 20px;
    color: var(--cyan);
    font-size: 44px;
    font-weight: 400;
    line-height: 1.1;
  }
  .contact-list {
    list-style: none;
    margin: 0;
    padding: 0;
  }
  .contact-item {
    display: flex;
    align-items: center;
    gap: 16px;
    font-size: 25px;
    line-height: 1;
    height: 40px;
    margin-bottom: 27px;
  }
  .contact-item.email { margin-bottom: 28px; }
  .contact-icon {
    width: 40px;
    height: 40px;
    flex: none;
  }
</style>
</head>
<body>
<main class="card">
  <svg class="card-backdrop" width="1200" height="791" viewBox="0 0 1200 791" aria-hidden="true">
    <defs>
      <linearGradient id="navyFade" x1="0" y1="0" x2="0" y2="1">
        <stop offset="0" stop-color="var(--navy)"/>
        <stop offset="1" stop-color="var(--navy-deep)"/>
      </linearGradient>
    </defs>
    <rect class="band" x="0" y="0" width="1200" height="791" fill="var(--royal)"/>
    <rect class="band" x="90" y="0" width="160" height="520" fill="var(--royal-mid)"/>
    <rect class="band" x="250" y="0" width="70" height="420" fill="var(--royal-light)" opacity="0.6"/>
    <rect class="band" x="530" y="110" width="150" height="300" fill="var(--royal-mid)"/>
    <rect class="band" x="690" y="0" width="110" height="280" fill="var(--royal-light)" opacity="0.5"/>
    <rect class="band" x="820" y="40" width="210" height="180" fill="var(--royal-mid)"/>
    <rect class="band" x="1040" y="0" width="160" height="160" fill="var(--royal-light)" opacity="0.6"/>
    <polygon class="lower-left" points="0,520 410,396 410,791 0,791" fill="url(#navyFade)"/>
    <polygon class="contact-panel" points="410,396 1200,156 1200,791 410,791" fill="var(--black)"/>
  </svg>

  <div class="brand">
    <span class="brand-square"></span>
    <p class="brand-name">BROOKCREST</p>
  </div>

  <section class="contact">
    <h1 class="company-name">Brookcrest Estates Limited</h1>
    <ul class="contact-list">
      <li class="contact-item address">
        <svg class="contact-icon" viewBox="0 0 40 40" aria-hidden="true">
          <path d="M20 6 L4 20 H9 V34 H17 V25 H23 V34 H31 V20 H36 Z" fill="var(--cyan)"/>
        </svg>
        <span>Unit 4, 15-17 Farrowby Lane London SE22 7QN</span>
      </li>
      <li class="contact-item web">
        <svg class="contact-icon" viewBox="0 0 40 40" aria-hidden="true">
          <circle cx="20" cy="20" r="16" fill="var(--cyan)"/>
          <circle cx="20" cy="20" r="16" fill="none" stroke="var(--black)" stroke-width="2"/>
          <ellipse cx="20" cy="20" rx="7" ry="16" fill="none" stroke="var(--black)" stroke-width="2"/>
          <line x1="4" y1="20" x2="36" y2="20" stroke="var(--black)" stroke-width="2"/>
        </svg>
        <span>www.brookcrestestates-example.com</span>
      </li>
      <li class="contact-item email">
        <svg class="contact-icon" viewBox="0 0 40 40" aria-hidden="true">
          <rect x="3" y="9" width="34" height="22" fill="var(--cyan)"/>
          <path d="M3 9 L20 23 L37 9" fill="none" stroke="var(--black)" stroke-width="2"/>
        </svg>
        <span>brookcrestltd@mailbox-example.com</span>
      </li>
      <li class="contact-item phone">
        <svg class="contact-icon" viewBox="0 0 40 40" aria-hidden="true">
          <circle cx="20" cy="20" r="17" fill="none" stroke="var(--cyan)" stroke-width="2.5"/>
          <path d="M14 10 L18 14 L16 17 C17 20 20 23 23 24 L26 22 L30 26 L27 30 C19 30 10 21 10 13 Z" fill="var(--cyan)"/>
        </svg>
        <span>+44-208-555-0142 +44-208-555-0187</span>
      </li>
    </ul>
  </section>
</main>
</body>
</html>
```